Modern and Luxury Cosmetics Re-Brand

Looking for a professional, modern, and minimal packaging design to replace current look. Must serve to appeal to both old and young customers.

Our products have 22+ sea and earth minerals, 12 of which are unique to only one location. Think about thousands of mineral particles actively antioxidizing the skin, rejuvenating and renewing it as it is exposed.

Target Market(s)

Cosmetics, Beauty Products

Industry/Entity Type

Cosmetic

Colors

Designer to choose colors to be used in the design.

Requirements
Must have
• Elegant and Unique look. Minimal and appealing.

```html
<!DOCTYPE html>
<html lang="en">
<head>
<meta charset="utf-8">
<title>Nuvara – Extremely Dry Skin Cream</title>
<link rel="stylesheet" href="https://fonts.googleapis.com/css2?family=Cinzel:wght@400;700&family=Cormorant+Garamond:ital,wght@0,700;1,400&family=PT+Sans:wght@400&display=swap">
<style>
  :root {
    --page: #ffffff;
    --silver-top: #f3f3f4;
    --silver-mid: #d3d4d6;
    --silver-bottom: #a4a5a8;
    --ink: #231f20;
    --mineral-blue: #12a3dc;
    --mineral-light: #bfe7f7;
    --gold-dark: #c28d45;
    --gold-light: #f4dc8c;
  }
  * { margin: 0; padding: 0; box-sizing: border-box; }
  html, body {
    width: 1000px; height: 1200px; overflow: hidden;
    background: var(--page);
  }
  .canvas { position: relative; width: 1000px; height: 1200px; }
  .label {
    position: absolute; left: 163px; top: 0; width: 674px; height: 1200px;
    background: linear-gradient(180deg, var(--silver-top) 0%, var(--silver-mid) 55%, var(--silver-bottom) 100%);
    overflow: hidden;
  }
  .minerals { position: absolute; left: 0; top: 0; width: 674px; height: 1200px; }
  .brand-dot {
    position: absolute; left: 325px; top: 60px; width: 44px; height: 44px;
    border-radius: 50%; background: var(--gold-dark);
  }
  .brand-name {
    position: absolute; left: 337px; top: 430px;
    transform: translate(-50%, -50%) rotate(-90deg);
    font-family: "Cormorant Garamond", serif; font-weight: 700;
    font-size: 176px; line-height: 1; color: var(--ink); white-space: nowrap;
  }
  .product {
    position: absolute; left: 0; width: 100%; text-align: center; color: var(--ink);
  }
  .product-type {
    top: 800px; font-family: "Cinzel", serif; font-weight: 400;
    font-size: 41px; line-height: 50px; letter-spacing: 1px;
  }
  .product-with {
    top: 910px; font-family: "Cormorant Garamond", serif; font-style: italic;
    font-size: 34px; line-height: 40px;
    display: flex; justify-content: center; align-items: center; gap: 14px;
  }
  .product-with .rule { width: 62px; height: 2px; background: var(--ink); }
  .product-key {
    top: 962px; font-family: "Cinzel", serif; font-weight: 700;
    font-size: 43px; line-height: 50px; letter-spacing: 1px;
  }
  .volume {
    top: 1095px; font-family: "PT Sans", sans-serif; font-size: 29px; line-height: 36px;
  }
  .volume .e-mark { font-size: 38px; margin: 0 12px; }
  .maker-band {
    position: absolute; left: 0; bottom: 0; width: 100%; height: 43px;
    background: linear-gradient(90deg, var(--gold-dark) 0%, var(--gold-light) 50%, var(--gold-dark) 100%);
    font-family: "PT Sans", sans-serif; font-size: 20px; line-height: 43px;
    text-align: center; color: var(--ink);
  }
</style>
</head>
<body>
<main class="canvas">
  <section class="label">
    <svg class="minerals" viewBox="163 0 674 1200" role="img" aria-label="Illustration of scattered blue faceted mineral crystals">
      <defs>
        <linearGradient id="crystal-tone" x1="0" y1="0" x2="0" y2="1">
          <stop offset="0" stop-color="var(--mineral-blue)"/>
          <stop offset="1" stop-color="var(--mineral-light)"/>
        </linearGradient>
      </defs>
      <path d="M163,0 L320,0 L330,130 L300,240 L335,330 L290,470 L300,560 L265,665 L200,640 L163,560 Z" fill="url(#crystal-tone)" opacity="0.85"/>
      <path d="M690,0 L837,0 L837,530 L790,525 L750,430 L715,350 L745,260 L710,210 L655,140 L700,60 Z" fill="url(#crystal-tone)" opacity="0.85"/>
    </svg>

    <span class="brand-dot" aria-hidden="true"></span>
    <h1 class="brand-name">Nuvara</h1>

    <p class="product product-type">EXTREMELY DRY<br>SKIN CREAM</p>
    <p class="product product-with"><span class="rule"></span>with<span class="rule"></span></p>
    <p class="product product-key">DEAD SEA MINERALS</p>

    <p class="product volume">200 ml<span class="e-mark">℮</span>3.38 oz</p>

    <footer class="maker-band">Parapharmaceuticals &amp; Cosmetics Factory</footer>
  </section>
</main>
</body>
</html>
```